Brochure required for large legal practice

We require a brochure, poster and PowerPoint to be designed to promote our new Employee Benefits Program to our employees. The brochure needs to be modern, clean and corporate. Our target market is solicitors, legal support staff and administration staff based across multiple sites in Queensland, Australia. Logos and brochure/poster content have been attached as well as a detailed brief.

Please note that several photos of our employees have now been uploaded and can be used in this material only.                             

Legal

```html
<!DOCTYPE html>
<html lang="en">
<head>
<meta charset="utf-8">
<title>Harlow Group Employee Benefits Brochure</title>
<link rel="stylesheet" href="https://fonts.googleapis.com/css2?family=Arimo:wght@400;700&display=swap">
<style>
  :root {
    --page-bg: #e9e7e4;
    --paper: #ffffff;
    --grey-band: #8f8e8a;
    --grey-light: #d6d5d2;
    --ink: #1b1b1b;
    --ink-soft: #3a3a3a;
    --brand: #6f6d68;
    --partner: #e2231a;
    --night: #1d1b1c;
    --photo-dark: #4a4f5a;
    --photo-mid: #9a9ea6;
    --photo-light: #e4e1dc;
  }
  * { box-sizing: border-box; margin: 0; padding: 0; }
  html, body { width: 818px; height: 1200px; overflow: hidden; }
  body { background: var(--page-bg); font-family: "Arimo", Arial, sans-serif; color: var(--ink); position: relative; }

  .spread { position: absolute; left: 25px; width: 770px; background: var(--paper); overflow: hidden; }
  .spread--cover { top: 38px; height: 542px; }
  .spread--inside { top: 620px; height: 545px; }
  .spread svg.shapes { position: absolute; inset: 0; width: 100%; height: 100%; }
  .spread .fold { position: absolute; top: 0; bottom: 0; width: 1px; background: rgba(0,0,0,.08); }

  .brand { position: absolute; display: flex; align-items: center; gap: 8px; white-space: nowrap; }
  .brand__mark { width: 12px; height: 12px; background: var(--brand); flex: none; }
  .brand__name { font-weight: 400; font-size: 20px; color: var(--brand); line-height: 1; letter-spacing: .5px; }

  .contact { position: absolute; left: 13px; top: 440px; width: 110px; font-size: 9px; line-height: 1.3; color: var(--ink); }

  .welcome { position: absolute; left: 88px; top: 330px; width: 282px; }
  .welcome h2 { font-size: 8px; font-weight: 700; margin-bottom: 5px; }
  .welcome p, .health p { font-size: 6px; line-height: 1.4; color: var(--ink-soft); margin-bottom: 4px; }

  .health { position: absolute; left: 395px; top: 126px; width: 345px; }
  .health h2 { font-size: 10px; font-weight: 700; margin-bottom: 4px; }
  .health h3 { font-size: 9px; font-weight: 700; margin: 10px 0 6px; }
  .health .partner { font-size: 26px; font-weight: 700; color: var(--partner); line-height: 1; margin-bottom: 18px; }
  .health .indent { padding-left: 10px; }
  .health ul { list-style: none; display: flex; gap: 22px; padding-left: 38px; font-size: 6px; color: var(--ink-soft); margin-bottom: 5px; white-space: nowrap; }
  .health li::before { content: "•"; margin-right: 8px; }
</style>
</head>
<body>

<section class="spread spread--cover">
  <svg class="shapes" viewBox="0 0 770 542" preserveAspectRatio="none">
    <defs>
      <linearGradient id="teamPhoto" x1="0" y1="0" x2="1" y2="1">
        <stop offset="0" stop-color="var(--photo-dark)"/>
        <stop offset=".6" stop-color="var(--photo-mid)"/>
        <stop offset="1" stop-color="var(--photo-light)"/>
      </linearGradient>
      <linearGradient id="officePhoto" x1="0" y1="0" x2="1" y2="1">
        <stop offset="0" stop-color="#3c4d8a"/>
        <stop offset=".5" stop-color="#b9b2a6"/>
        <stop offset="1" stop-color="#d9d4cc"/>
      </linearGradient>
    </defs>
    <path d="M0 300 Q200 262 385 200 V216 Q200 278 0 316 Z" fill="var(--grey-light)"/>
    <path d="M0 0 H385 V200 Q200 262 0 300 Z" fill="url(#teamPhoto)" role="img" aria-label="Photo of several hands joining jigsaw puzzle pieces"/>
    <path d="M0 488 Q50 510 110 542 H0 Z" fill="var(--grey-light)"/>
    <path d="M110 542 Q250 478 385 408 V542 Z" fill="var(--grey-band)"/>

    <path d="M385 70 Q570 56 770 72 V86 Q570 70 385 84 Z" fill="var(--grey-light)"/>
    <path d="M385 82 Q570 68 770 84 V542 H385 Z" fill="url(#officePhoto)" role="img" aria-label="Photo of two smiling employees seated at an office table"/>
    <path d="M470 542 Q600 340 770 300 V542 Z" fill="var(--grey-light)" stroke="var(--paper)" stroke-width="2"/>
    <path d="M385 382 Q480 370 545 542 H385 Z" fill="var(--grey-band)" stroke="var(--paper)" stroke-width="2"/>
    <path d="M430 542 Q480 420 540 398 Q630 430 690 542 Z" fill="var(--night)" stroke="var(--paper)" stroke-width="2"/>
    <path d="M640 542 Q680 420 770 362 V542 Z" fill="var(--paper)"/>
  </svg>
  <div class="fold" style="left:385px"></div>

  <div class="brand" style="left:13px; top:400px;">
    <span class="brand__mark"></span><span class="brand__name">Harlow Group</span>
  </div>
  <p class="contact">Put your contact information and address here</p>

  <div class="brand" style="left:620px; top:40px;">
    <span class="brand__mark"></span><span class="brand__name">Harlow Group</span>
  </div>
</section>

<section class="spread spread--inside">
  <svg class="shapes" viewBox="0 0 770 545" preserveAspectRatio="none">
    <defs>
      <linearGradient id="meetingPhoto" x1="0" y1="0" x2="1" y2="1">
        <stop offset="0" stop-color="#b7b2aa"/>
        <stop offset=".5" stop-color="#d8dde4"/>
        <stop offset="1" stop-color="#eef0f2"/>
      </linearGradient>
      <linearGradient id="pageShade" x1="0" y1="0" x2="1" y2="0">
        <stop offset="0" stop-color="#ffffff"/>
        <stop offset=".5" stop-color="#f3f3f3"/>
        <stop offset="1" stop-color="#d9d9d9"/>
      </linearGradient>
    </defs>
    <rect x="0" y="0" width="400" height="545" fill="url(#pageShade)"/>
    <path d="M0 140 Q160 180 250 250 Q100 300 0 420 Z" fill="var(--grey-band)"/>
    <path d="M0 0 H400 V80 Q300 140 225 215 Q120 160 0 145 Z" fill="url(#meetingPhoto)" role="img" aria-label="Photo of a man and a woman in a meeting at an office table"/>
    <path d="M400 0 Q330 120 260 230 L250 250 Q330 150 400 110 Z" fill="var(--grey-light)"/>

    <path d="M400 0 H620 Q520 45 470 62 Q430 30 400 0 Z" fill="var(--night)"/>
    <path d="M620 0 H770 V55 Q620 30 500 70 Q560 30 620 0 Z" fill="var(--grey-band)"/>
    <path d="M400 0 Q460 60 560 90 Q470 95 400 110 Z" fill="var(--grey-light)"/>
    <path d="M560 90 Q660 50 770 55 V80 Q660 70 560 90 Z" fill="var(--grey-light)"/>
    <rect x="460" y="320" width="233" height="208" fill="#eceae6" role="img" aria-label="Screenshot of the health insurer's website offering the staff discount"/>
  </svg>
  <div class="fold" style="left:400px"></div>

  <div class="brand" style="left:180px; top:280px;">
    <span class="brand__mark"></span><span class="brand__name">Harlow Group</span>
  </div>

  <article class="welcome">
    <h2>Welcome to the Harlow Group Employee Benefits Program.</h2>
    <p>Harlow Group aims to foster a relaxed and warm culture emphasising teamwork and the celebration of achievement.</p>
    <p>We value our employees and have, therefore, designed an Employee Benefits Program to both express thanks and reward our people for their ongoing loyalty and dedication.</p>
    <p>Our Employee Benefits program also follows our belief that everyone benefits from a healthy work/life balance in order to continue to grow and prosper both professionally and personally.</p>
    <p>The program contains a wide range of benefits including health initiatives, financial savings, social events and activities, shopping and travel discounts as well as rewards for length of service and contribution.</p>
    <p>Employees of Harlow Group and its subsidiaries (“Employees”) who have successfully completed their probationary period and who are employed on a permanent or long term casual basis are eligible to take part in our Employee Benefits Program.</p>
    <p>For more information, please see the terms and conditions for each item, or see a member of the Human Resources team.</p>
    <p>Terms and conditions are accurate as at the time of going to print, but since the availability of these benefits is determined by our affiliated service providers, we cannot guarantee that any of the benefits will be offered on a long-term basis. From time to time, any of the benefits currently advertised may change without prior warning, and some may be discontinued altogether. Whilst we have no control over these changes, we will notify Employees as they come to our attention.</p>
  </article>

  <article class="health">
    <h2>Health Benefits</h2>
    <p>The health and wellness of our Employees is important to us and we are committed to providing a range of benefits to help our employees lead healthier lives.</p>
    <h3>Discounted Health Insurance</h3>
    <div class="partner">Vitacare</div>
    <div class="indent">
      <p>Employees receive an 8.3% discount on a range of coverage options provided by Vitacare.</p>
      <p>For Employees that take out both corporate hospital and extras cover, Corporate Premier Health Cover or any Working Visa Health Insurance within the first 3 months of commencing their employment with Harlow Group or one of its subsidiaries, Vitacare will also waive the 2 &amp; 6 month waiting periods on extras.</p>
      <p>As Vitacare members, Employees will also receive a 10% discount on the following products:</p>
    </div>
    <ul>
      <li>Travel Insurance</li><li>Pet Insurance</li><li>Life Insurance</li><li>Income Protection Insurance.</li>
    </ul>
    <p class="indent">For further information, Employees can call the Vitacare Corporate Hotline on //*// or visit the online member portal at //*//.</p>
  </article>
</section>

</body>
</html>
```